Delcourt Realty Business Cards

Design business card

Target Market(s)

High-End Buyer of Real Estate over $1 million dollars

Industry/Entity Type

Realtor

Contact Information for Business Card

Lena Delcourt R(S) LIC.# 41972
Cell 555 246-1938
Email Lena@Delcourt.example
Website IsleFreshHomes.example

Also Need Cards for:

Hank Delcourt R(B) LIC# 69418
C 555 613-7052
E Hank@Delcourt.example
W IsleFreshHomes.example

Colors

Designer to choose colors to be used in the design.

Requirements
Must have
• Address on back:
• 287 Pohaku Cir. , Lanikoa HI 96799
• Logo on back
Nice to have
• I would like the phone numbers and email address to be big so people can read it easily
Should not have
• Very small print Except For: address (287 Pohaku Cir. Wailea HI 96753)

```html
<!DOCTYPE html>
<html lang="en">
<head>
<meta charset="utf-8">
<title>Delcourt Realty Business Cards</title>
<link href="https://fonts.googleapis.com/css2?family=Mulish:wght@300;400;700;800&display=swap" rel="stylesheet">
<style>
  :root {
    --backdrop: #d8d8d8;
    --charcoal: #2c2b2c;
    --paper: #f7f6f2;
    --sand: #d5d2c4;
    --ink: #2a2a2a;
    --ink-soft: #4a4a48;
    --white: #ffffff;
  }
  * { margin: 0; padding: 0; box-sizing: border-box; }
  html, body { width: 1200px; height: 1200px; overflow: hidden; }
  body {
    background: var(--backdrop);
    font-family: "Mulish", sans-serif;
    color: var(--ink);
    position: relative;
  }
  .card {
    position: absolute;
    left: 250px;
    width: 700px;
    height: 400px;
    border-radius: 4px;
    box-shadow: 0 6px 18px rgba(0,0,0,0.12);
  }

  /* Back of card */
  .card-back {
    top: 150px;
    background: var(--charcoal);
    color: var(--white);
  }
  .card-back .brand {
    position: absolute;
    top: 135px;
    left: 0; right: 0;
    display: flex;
    align-items: center;
    justify-content: center;
    gap: 22px;
  }
  .card-back .brand-mark {
    width: 30px; height: 30px;
    background: var(--white);
  }
  .card-back .brand-name {
    font-weight: 800;
    font-size: 44px;
    letter-spacing: 5px;
    text-transform: uppercase;
  }
  .card-back .address {
    position: absolute;
    top: 262px;
    left: 0; right: 0;
    text-align: center;
    font-weight: 400;
    font-size: 21px;
    letter-spacing: 1px;
  }

  /* Front of card */
  .card-front {
    top: 650px;
    background: var(--paper);
    padding: 22px;
  }
  .card-front .panel {
    position: relative;
    width: 100%;
    height: 100%;
    background: var(--sand);
  }
  .card-front .brand {
    position: absolute;
    top: 20px;
    right: 26px;
    display: flex;
    align-items: center;
    gap: 10px;
  }
  .card-front .brand-mark {
    width: 16px; height: 16px;
    background: var(--charcoal);
  }
  .card-front .brand-name {
    font-weight: 800;
    font-size: 19px;
    letter-spacing: 1.5px;
    text-transform: uppercase;
    color: var(--charcoal);
  }
  .card-front .accent-block {
    position: absolute;
    left: 0;
    top: 158px;
    width: 40px;
    height: 60px;
    background: var(--charcoal);
  }
  .card-front .agent-name {
    position: absolute;
    left: 96px;
    top: 122px;
    font-size: 36px;
    font-weight: 300;
    line-height: 1;
  }
  .card-front .agent-name strong { font-weight: 800; }
  .card-front .license {
    position: absolute;
    left: 96px;
    top: 178px;
    font-size: 20px;
    font-weight: 400;
    color: var(--ink-soft);
  }
  .card-front .rule {
    position: absolute;
    left: 96px;
    right: 26px;
    height: 2px;
    background: var(--ink);
  }
  .card-front .rule-top { top: 164px; }
  .card-front .rule-bottom { top: 242px; }
  .card-front .contact-line {
    position: absolute;
    left: 96px;
    right: 26px;
    top: 256px;
    font-size: 22px;
    font-weight: 400;
    white-space: nowrap;
  }
  .card-front .contact-line b { font-weight: 800; font-size: 26px; }
  .card-front .contact-line .sep { margin: 0 10px; font-weight: 800; }
  .card-front .website {
    position: absolute;
    left: 96px;
    right: 26px;
    top: 300px;
    text-align: center;
    font-size: 22px;
    font-weight: 800;
    letter-spacing: 0.5px;
  }
</style>
</head>
<body>

  <section class="card card-back" aria-label="Card back">
    <div class="brand">
      <span class="brand-mark"></span>
      <span class="brand-name">Delcourt Realty</span>
    </div>
    <p class="address">287 Pohaku Cir. , Lanikoa HI 96799</p>
  </section>

  <section class="card card-front" aria-label="Card front">
    <div class="panel">
      <div class="brand">
        <span class="brand-mark"></span>
        <span class="brand-name">Delcourt Realty</span>
      </div>
      <span class="accent-block"></span>
      <h1 class="agent-name">Lena <strong>Delcourt</strong></h1>
      <span class="rule rule-top"></span>
      <p class="license">R(S) LIC.# 41972</p>
      <span class="rule rule-bottom"></span>
      <p class="contact-line"><b>C</b> - 555 246-1938<span class="sep">•</span><b>E</b> - Lena@Delcourt.example</p>
      <p class="website">www.IsleFreshHomes.example</p>
    </div>
  </section>

</body>
</html>
```